Restaurant, Nightclub

It's a Restaurant come nightclub. Our sign Tamsel is white letters with blue edging on a black back ground.

Industry/Entity Type

Restaurant

Contact Information for Business Card

Tamsel Stevenage Ltd
14 Larkfield Row
Stevenage Herts KX7 2PW

```html
<!DOCTYPE html>
<html lang="en">
<head>
<meta charset="utf-8">
<title>Tamsel Stevenage Ltd — Business Card</title>
<link rel="stylesheet" href="https://fonts.googleapis.com/css2?family=Cormorant+Garamond:wght@500;600&display=swap">
<style>
  :root {
    --page-bg: #e6e4e1;
    --card-black: #0b0b0c;
    --leather-top: #1c1c1e;
    --leather-low: #2a2a2c;
    --band-black: #000000;
    --accent-cyan: #3ec3e6;
    --text-white: #f4f4f4;
    --text-soft: #d9d9d9;
  }
  * { margin: 0; padding: 0; box-sizing: border-box; }
  html, body {
    width: 1200px;
    height: 716px;
    overflow: hidden;
    background: var(--page-bg);
  }
  .canvas {
    width: 1200px;
    height: 716px;
    display: flex;
    align-items: center;
    justify-content: center;
  }
  .business-card {
    position: relative;
    width: 880px;
    height: 520px;
    background: var(--card-black);
    overflow: hidden;
    box-shadow: 0 14px 34px rgba(0, 0, 0, 0.28);
    font-family: "Cormorant Garamond", Georgia, serif;
    color: var(--text-white);
  }
  .logo-panel {
    position: absolute;
    left: 0; top: 0;
    width: 100%;
    height: 248px;
    background: linear-gradient(180deg, var(--leather-top) 0%, #121213 100%);
    display: flex;
    align-items: center;
    justify-content: center;
  }
  .logo-panel::after {
    content: "";
    position: absolute;
    left: 0; right: 0; bottom: 0;
    height: 22px;
    background: linear-gradient(180deg, rgba(0,0,0,0) 0%, rgba(0,0,0,0.55) 100%);
  }
  .brand-name {
    font-size: 168px;
    font-weight: 600;
    line-height: 1;
    color: var(--text-white);
    letter-spacing: 2px;
  }
  .company-band {
    position: absolute;
    left: 0; top: 248px;
    width: 100%;
    height: 100px;
    background: var(--band-black);
    text-align: center;
    padding-top: 10px;
  }
  .company-name {
    font-size: 40px;
    font-weight: 500;
    line-height: 1.1;
  }
  .company-address {
    font-size: 31px;
    font-weight: 500;
    line-height: 1.25;
    letter-spacing: 0.5px;
  }
  .accent-stripe {
    position: absolute;
    left: 0; top: 348px;
    width: 100%;
    height: 14px;
    background: var(--accent-cyan);
  }
  .contact-panel {
    position: absolute;
    left: 0; top: 362px;
    width: 100%;
    height: 158px;
    background: radial-gradient(ellipse at 50% 30%, var(--leather-low) 0%, #161617 75%);
    text-align: center;
    padding-top: 26px;
  }
  .contact-line {
    font-size: 27px;
    font-weight: 500;
    line-height: 1.3;
    color: var(--text-soft);
  }
</style>
</head>
<body>
  <main class="canvas">
    <article class="business-card">
      <header class="logo-panel">
        <span class="brand-name">Tamsel</span>
      </header>
      <section class="company-band">
        <p class="company-name">Tamsel Stevenage Ltd</p>
        <p class="company-address">14 Larkfield Row Stevenage Herts KX7 2PW</p>
      </section>
      <div class="accent-stripe"></div>
      <footer class="contact-panel">
        <p class="contact-line">www.TamselStevenage.com</p>
        <p class="contact-line">info@TamselStevenage.co.uk</p>
      </footer>
    </article>
  </main>
</body>
</html>
```